Brell Harbor Company Business Cards

Front and Back Business Card - logo and text setup - cool design. I need workable photoshop or illustrator files so I can setup each employee card with design that is created
Updates

Hi everyone, thank you for the great entries. Please no more white and blue cards - there are so many already - black and silver only now please. thanks!

Target Market(s)

Construction Industry - Facility Managers

Industry/Entity Type

Construction

Contact Information for Business Card

I really like contemporary simplistic looks - clean neat....not opposed to seeing some black backrounds

Requirements
Must have
• Logo/website address with design on front only - www.brellharbor-example.com (logo attached)
• Back:
• Name/Title/Company Address/Phone/email address
Nice to have
• Cool design
Should not have
• Nothing gimmicky like Fire or Water - since we are a Fire Protection company - it has all been done

```html
<!DOCTYPE html>
<html lang="en">
<head>
<meta charset="utf-8">
<title>Brell Harbor Company – Business Cards</title>
<link rel="stylesheet" href="https://fonts.googleapis.com/css2?family=Montserrat:wght@500;700;800&display=swap">
<style>
  :root {
    --page-bg: #e9e6e1;
    --card-dark: #141414;
    --card-mid: #262626;
    --stripe: rgba(255,255,255,0.035);
    --brand-blue: #3b64ad;
    --accent-red: #d8353a;
    --text-light: #e8e8e8;
    --text-muted: #9a9a9a;
  }
  * { box-sizing: border-box; margin: 0; padding: 0; }
  html, body { width: 1200px; height: 1200px; overflow: hidden; }
  body {
    background: var(--page-bg);
    font-family: "Montserrat", sans-serif;
    position: relative;
  }
  .card {
    position: absolute;
    left: 180px;
    width: 840px;
    height: 480px;
    border-radius: 6px;
    overflow: hidden;
    background:
      repeating-linear-gradient(135deg, var(--stripe) 0 2px, transparent 2px 6px),
      linear-gradient(160deg, var(--card-mid) 0%, var(--card-dark) 55%, #0c0c0c 100%);
    box-shadow: 0 12px 30px rgba(0,0,0,0.28);
  }
  .card--front { top: 70px; }
  .card--back { top: 650px; }

  .brand-name {
    color: var(--brand-blue);
    font-weight: 800;
    letter-spacing: -0.5px;
    line-height: 1;
    display: flex;
    align-items: center;
  }
  .brand-name .brand-dot {
    display: inline-block;
    background: var(--accent-red);
    border-radius: 50%;
    flex: none;
  }

  /* Front */
  .front-brand {
    position: absolute;
    left: 90px;
    top: 150px;
    font-size: 64px;
    gap: 22px;
  }
  .front-brand .brand-dot { width: 26px; height: 26px; }
  .front-web {
    position: absolute;
    left: 90px;
    right: 90px;
    top: 340px;
    display: flex;
    align-items: center;
    gap: 18px;
  }
  .front-web .rule { flex: 1; height: 2px; background: var(--accent-red); opacity: 0.7; }
  .front-web .url { color: var(--text-muted); font-size: 20px; font-weight: 500; letter-spacing: 0.5px; }

  /* Back */
  .back-brand {
    position: absolute;
    right: 60px;
    top: 50px;
    font-size: 30px;
    gap: 12px;
  }
  .back-brand .brand-dot { width: 14px; height: 14px; }
  .person {
    position: absolute;
    left: 60px;
    top: 140px;
    padding-left: 22px;
    border-left: 4px solid var(--accent-red);
  }
  .person .name { color: var(--text-light); font-size: 28px; font-weight: 700; }
  .person .title { color: var(--text-muted); font-size: 20px; font-weight: 500; margin-top: 6px; }
  .contacts {
    position: absolute;
    left: 60px;
    top: 260px;
    list-style: none;
  }
  .contacts li, .address {
    display: flex;
    align-items: center;
    gap: 14px;
    color: var(--text-light);
    font-size: 19px;
    font-weight: 500;
    margin-bottom: 12px;
  }
  .icon {
    width: 32px;
    height: 32px;
    border-radius: 50%;
    background: var(--accent-red);
    display: flex;
    align-items: center;
    justify-content: center;
    flex: none;
  }
  .icon svg { width: 18px; height: 18px; }
  .address {
    position: absolute;
    left: 60px;
    bottom: 40px;
    margin: 0;
  }
</style>
</head>
<body>

<section class="card card--front" aria-label="Business card front">
  <div class="brand-name front-brand"><span class="brand-dot"></span>Brell Harbor Company</div>
  <div class="front-web">
    <span class="rule"></span>
    <span class="url">www.brellharbor-example.com</span>
    <span class="rule"></span>
  </div>
</section>

<section class="card card--back" aria-label="Business card back">
  <div class="brand-name back-brand"><span class="brand-dot"></span>Brell Harbor Company</div>

  <div class="person">
    <p class="name">Dana Wells Carver</p>
    <p class="title">President</p>
  </div>

  <ul class="contacts">
    <li>
      <span class="icon"><svg viewBox="0 0 24 24" fill="#fff"><path d="M6.6 10.8a15.1 15.1 0 0 0 6.6 6.6l2.2-2.2c.3-.3.7-.4 1-.2 1.1.4 2.3.6 3.6.6.6 0 1 .4 1 1V20c0 .6-.4 1-1 1A17 17 0 0 1 3 4c0-.6.4-1 1-1h3.5c.6 0 1 .4 1 1 0 1.3.2 2.5.6 3.6.1.3 0 .7-.2 1z"/></svg></span>
      (555) 014-2290
    </li>
    <li>
      <span class="icon"><svg viewBox="0 0 24 24" fill="none" stroke="#fff" stroke-width="2"><rect x="3" y="5" width="18" height="14" rx="1"/><path d="M3 6l9 7 9-7"/></svg></span>
      dana@brellharbor-example.com
    </li>
    <li>
      <span class="icon"><svg viewBox="0 0 24 24" fill="none" stroke="#fff" stroke-width="2"><circle cx="12" cy="12" r="9"/><path d="M3 12h18M12 3c3 3 3 15 0 18M12 3c-3 3-3 15 0 18"/></svg></span>
      www.brellharbor-example.com
    </li>
  </ul>

  <p class="address">
    <span class="icon"><svg viewBox="0 0 24 24" fill="#fff"><path d="M12 2a7 7 0 0 0-7 7c0 5 7 13 7 13s7-8 7-13a7 7 0 0 0-7-7zm0 9.5A2.5 2.5 0 1 1 12 6.5a2.5 2.5 0 0 1 0 5z"/></svg></span>
    12 Harbor Point Dr. Lakeview, NY 10000
  </p>
</section>

</body>
</html>
```